Break The Chain by Lena Varo

I am the Founder of a Not For Profit and writing a book about my story to raise funds for the work we do within our community.

It is my first book and would like a really cool cover, the title is:

BREAK THE CHAIN BEFORE IT BINDS YOU - How I Rebuilt a Life Through Cravings, Mania and Despair.

Author: Lena Varo

I plan to release the Quillo and Tunora copy on December 24, 2013 to commemorate the passing of my beloved Father in 2009 and this would make him very proud.

I need a book cover now so I can start marketing, here is Chapter List to give you a flavour:

Chapter One - Addiction Epidemic Worldwide

Chapter Two - Bipolar Kills

Chapter Three - Surviving Suicide

Chapter Four - Recovery Goals

Chapter Five – Healing Oneself

Chapter Six – Spirituality as the Key to Healing

Chapter Seven – Living a Life of Purpose

I have also uploaded current Best Sellers on Bookvale. I want the text to be: Purple and Yellow for BREAK THE CHAIN (My Charity colours). Please check out the website as well to get a feel for what I believe and stand for. The book pre-order is in the website too so I really need money to raise funds. Charity is Down to nothing at all! But as you can imagine the clients have addiction problems hence only efforts like book sales really guarantee or generate us any money as a Charity.

www.GuidanceOnRiverbend.Org.Au

I also want on the background to be Filipino flag components as that is where I was born. So red, blue, a big yellow sun and 3 yellow stars (attached flag to give you idea)

I have lots of pics so uploaded two that I think I want to use with cover.

Please please HELP!!!!!!

PS. The Velmora book is currently selling up to 300 - 500 copies daily and I did not particularly think it was a good cover therefore must be a good book.

Target Market(s)

20's - early 30's, disposable income, Asians, maybe living in US / Canada / Australia / Europe or travelled overseas with addiction issues / mental health issues.

Colors
ec2027
3276b5
6e489d
fbed23

Requirements
Must have
• Colours of the Philippines Flag as I am marketing to Filipinos predominantly, especially as that is where I am born.
Nice to have
• Bold Title like in Standing Tallish Book attached:

BREAK THE CHAIN BEFORE IT BINDS YOU

```html
<!DOCTYPE html>
<html lang="en">
<head>
<meta charset="utf-8">
<title>Break The Chain – Before It Binds You · Lena Varo</title>
<link rel="stylesheet" href="https://fonts.googleapis.com/css2?family=Amatic+SC:wght@700&family=Alegreya:ital@1&family=Fondamento&display=swap">
<style>
  :root {
    --ink: #0a0520;
    --title-yellow: #f7ea4a;
    --rule-yellow: #b9ad2c;
    --photo-light: #cfcac4;
    --photo-mid: #8d8782;
    --photo-dark: #2e2a28;
    --flag-blue: #3276b5;
    --flag-red: #ec2027;
    --flag-white: #ffffff;
    --flag-yellow: #fbed23;
  }
  html, body {
    margin: 0;
    padding: 0;
    width: 1200px;
    height: 806px;
    overflow: hidden;
    background: #ffffff;
  }
  .cover-spread {
    position: relative;
    width: 1200px;
    height: 806px;
    background: var(--ink);
    overflow: hidden;
  }
  .front-photo {
    position: absolute;
    left: 0;
    top: 0;
    width: 566px;
    height: 806px;
    background:
      radial-gradient(ellipse 300px 360px at 290px 300px, var(--photo-light), transparent 70%),
      linear-gradient(160deg, var(--photo-dark) 0%, var(--photo-mid) 35%, var(--photo-light) 60%, var(--photo-mid) 80%, var(--photo-dark) 100%);
  }
  .title {
    position: absolute;
    margin: 0;
    color: var(--title-yellow);
    font-family: "Amatic SC", "Arial Narrow", sans-serif;
    font-weight: 700;
    text-align: center;
    line-height: 1;
    white-space: nowrap;
  }
  .rule {
    position: absolute;
    height: 2px;
    background: linear-gradient(90deg, transparent, var(--rule-yellow) 15%, var(--rule-yellow) 85%, transparent);
  }
  .subtitle {
    position: absolute;
    margin: 0;
    color: var(--title-yellow);
    font-family: "Alegreya", Georgia, serif;
    font-style: italic;
    text-align: center;
    white-space: nowrap;
    line-height: 1;
  }
  /* front panel */
  .front .title-main { left: 0; width: 566px; top: 60px; font-size: 76px; }
  .front .rule-1 { left: 70px; width: 420px; top: 131px; }
  .front .title-sub { left: 0; width: 566px; top: 170px; font-size: 76px; }
  .front .rule-2 { left: 70px; width: 420px; top: 241px; }
  .front .subtitle { left: 0; width: 566px; top: 266px; font-size: 19px; }
  .author {
    position: absolute;
    left: 0;
    width: 566px;
    top: 640px;
    margin: 0;
    text-align: center;
    font-family: "Fondamento", Georgia, serif;
    font-size: 56px;
    line-height: 1;
    color: var(--title-yellow);
    text-shadow: 2px 2px 3px #000;
    word-spacing: 18px;
  }
  /* spine */
  .spine-title {
    position: absolute;
    left: 601px;
    top: 335px;
    margin: 0;
    transform: translate(-50%, -50%) rotate(-90deg);
    color: var(--title-yellow);
    font-family: "Amatic SC", "Arial Narrow", sans-serif;
    font-weight: 700;
    font-size: 46px;
    line-height: 1;
    white-space: nowrap;
    word-spacing: 2px;
  }
  .spine-title .gap { display: inline-block; width: 24px; }
  .spine-flag {
    position: absolute;
    left: 570px;
    top: 658px;
    width: 62px;
    height: 124px;
  }
  /* back panel */
  .back .title-main { left: 640px; width: 550px; top: 236px; font-size: 82px; }
  .back .rule-1 { left: 690px; width: 450px; top: 320px; }
  .back .title-sub { left: 640px; width: 550px; top: 360px; font-size: 82px; }
  .back .rule-2 { left: 690px; width: 450px; top: 444px; }
  .back .subtitle { left: 640px; width: 550px; top: 464px; font-size: 19px; }
</style>
</head>
<body>
<main class="cover-spread">
  <section class="front">
    <div class="front-photo" role="img" aria-label="Black and white portrait photograph of the author wearing a wide-brimmed straw hat"></div>
    <h1 class="title title-main">Break The Chain</h1>
    <div class="rule rule-1"></div>
    <p class="title title-sub">- Before It Binds You</p>
    <div class="rule rule-2"></div>
    <p class="subtitle">How I Rebuilt a Life Through Cravings, Mania and Despair</p>
    <p class="author">Lena Varo</p>
  </section>

  <section class="spine">
    <p class="spine-title">Break The Chain<span class="gap"></span>-Before It Binds You</p>
    <svg class="spine-flag" viewBox="0 0 62 124" aria-label="Philippine flag">
      <rect x="0" y="0" width="31" height="124" fill="var(--flag-blue)"/>
      <rect x="31" y="0" width="31" height="124" fill="var(--flag-red)"/>
      <polygon points="31,64 62,124 0,124" fill="var(--flag-white)"/>
      <circle cx="31" cy="104" r="7" fill="var(--flag-yellow)"/>
      <polygon points="31,74 32,77 35,77 32.6,78.8 33.5,81.8 31,80 28.5,81.8 29.4,78.8 27,77 30,77" fill="var(--flag-yellow)"/>
      <polygon points="10,112 11,115 14,115 11.6,116.8 12.5,119.8 10,118 7.5,119.8 8.4,116.8 6,115 9,115" fill="var(--flag-yellow)"/>
      <polygon points="52,112 53,115 56,115 53.6,116.8 54.5,119.8 52,118 49.5,119.8 50.4,116.8 48,115 51,115" fill="var(--flag-yellow)"/>
    </svg>
  </section>

  <section class="back">
    <h2 class="title title-main">Break The Chain</h2>
    <div class="rule rule-1"></div>
    <p class="title title-sub">-Before It Binds You</p>
    <div class="rule rule-2"></div>
    <p class="subtitle">How I Rebuilt a Life Through Cravings, Mania and Despair</p>
  </section>
</main>
</body>
</html>
```